Business card for auto dealership

Looking for a clean modern design.
Would like attached logo incorporated

Industry/Entity Type

Car dealership

Contact Information for Business Card

Name, website, phone, cell, fax, email

```html
<!DOCTYPE html>
<html lang="en">
<head>
<meta charset="UTF-8">
<title>Halden Truck &amp; Auto Sales – Business Card</title>
<link href="https://fonts.googleapis.com/css2?family=Lato:wght@400;700&display=swap" rel="stylesheet">
<style>
  :root {
    --stage: #c9c9c9;
    --card: #1d1d1d;
    --card-back: #141414;
    --edge: #c8151b;
    --ink: #ffffff;
    --accent: #d0262d;
    --rule: #6a6a6a;
    --deboss: #2e2e2e;
  }
  * { margin: 0; padding: 0; box-sizing: border-box; }
  html, body {
    width: 1200px;
    height: 1051px;
    overflow: hidden;
    background: var(--stage);
    font-family: "Lato", sans-serif;
  }
  .stage {
    width: 1200px;
    height: 1051px;
    display: flex;
    flex-direction: column;
    align-items: center;
    justify-content: center;
    gap: 60px;
  }
  .card {
    width: 700px;
    height: 400px;
    position: relative;
    border-bottom: 5px solid var(--edge);
    box-shadow: 0 14px 30px rgba(0,0,0,0.25);
  }
  .card--front {
    background: var(--card);
    display: flex;
    align-items: center;
  }
  .card--back {
    background: var(--card-back);
    display: flex;
    align-items: center;
    justify-content: center;
  }
  .brand {
    width: 340px;
    display: flex;
    flex-direction: column;
    align-items: center;
    color: var(--ink);
  }
  .brand__name {
    font-weight: 700;
    font-size: 54px;
    line-height: 1;
    color: var(--ink);
  }
  .brand__tagline {
    margin-top: 8px;
    font-weight: 700;
    font-size: 15px;
    letter-spacing: 1px;
    color: var(--accent);
    text-transform: uppercase;
  }
  .divider {
    width: 1px;
    height: 230px;
    background: var(--rule);
  }
  .details {
    padding-left: 40px;
    color: var(--ink);
  }
  .details__name {
    font-weight: 700;
    font-size: 30px;
    line-height: 1.1;
  }
  .details__title {
    font-size: 21px;
    color: var(--accent);
    margin-bottom: 26px;
  }
  .contact {
    list-style: none;
  }
  .contact__item {
    display: flex;
    align-items: center;
    gap: 12px;
    font-size: 19px;
    line-height: 1.45;
  }
  .contact__icon {
    width: 16px;
    height: 16px;
    flex: none;
    fill: none;
    stroke: var(--accent);
    stroke-width: 1.8;
  }
  .deboss__name {
    font-weight: 700;
    font-size: 120px;
    color: var(--deboss);
    line-height: 1;
  }
</style>
</head>
<body>
<main class="stage">
  <section class="card card--front" aria-label="Card front">
    <div class="brand">
      <span class="brand__name">Halden</span>
      <span class="brand__tagline">Truck &amp; Auto Sales</span>
    </div>
    <div class="divider"></div>
    <div class="details">
      <p class="details__name">Riley Halden</p>
      <p class="details__title">Managing Director</p>
      <ul class="contact">
        <li class="contact__item">
          <svg class="contact__icon" viewBox="0 0 16 16" aria-hidden="true"><path d="M3 1.5l3 3-1.5 2a8 8 0 0 0 5 5l2-1.5 3 3-2 2C6 14 2 10 1.5 3.5z"/></svg>
          555-014-2207
        </li>
        <li class="contact__item">
          <svg class="contact__icon" viewBox="0 0 16 16" aria-hidden="true"><rect x="4" y="1" width="8" height="14" rx="1.5"/><line x1="7" y1="12.5" x2="9" y2="12.5"/></svg>
          555-019-3368
        </li>
        <li class="contact__item">
          <svg class="contact__icon" viewBox="0 0 16 16" aria-hidden="true"><rect x="1" y="3" width="14" height="10"/><path d="M1 3l7 6 7-6"/></svg>
          riley@haldenauto.com
        </li>
        <li class="contact__item">
          <svg class="contact__icon" viewBox="0 0 16 16" aria-hidden="true"><circle cx="8" cy="8" r="6.5"/><ellipse cx="8" cy="8" rx="3" ry="6.5"/><line x1="1.5" y1="8" x2="14.5" y2="8"/></svg>
          www.haldenauto.com
        </li>
      </ul>
    </div>
  </section>

  <section class="card card--back" aria-label="Card back">
    <span class="deboss__name">Halden</span>
  </section>
</main>
</body>
</html>
```